Design a Mobile App for Landscape Businesses

This project is to design the first three screens for a mobile app for Landscape and Lawncare businesses. This app will serve as a directory for homeowners to locate landscape and lawn care businesses and for landscape businesses and contractors to run their business. See the attached PDF for more information and example
Here is the link to the description https://lnkshrt.example/q7Tz3K

Target Market(s)

Landscape and lawn care business, gardeners, home owners

Industry/Entity Type

Landscape Gardening

Logo Text

Velmarigo

Colors

Designer to choose colors to be used in the design.

```html
<!DOCTYPE html>
<html lang="en">
<head>
<meta charset="utf-8">
<title>Velmarigo – App Screens</title>
<link rel="stylesheet" href="https://fonts.googleapis.com/css2?family=Roboto:wght@300;400;500;700&display=swap">
<style>
:root{
  --bg:#e4e6ea;
  --screen:#ffffff;
  --ink:#1d1f22;
  --muted:#8d9197;
  --line:#e3e5e8;
  --green:#2fc94f;
  --green-dark:#1fae3d;
  --star:#f2641c;
  --icon-grey:#c9ccd0;
  --leaf-light:#8ccf4a;
  --leaf-dark:#1f5a1c;
}
*{box-sizing:border-box;margin:0;padding:0}
html,body{width:1200px;height:1197px;overflow:hidden}
body{background:var(--bg);font-family:"Roboto",Arial,sans-serif;color:var(--ink);position:relative}
.screen{position:absolute;width:340px;height:555px;background:var(--screen);border-radius:22px;overflow:hidden;box-shadow:0 14px 30px rgba(40,50,60,.12)}
.screen--profile{left:40px;top:30px}
.screen--business{left:410px;top:30px}
.screen--listing{left:40px;top:610px}
.screen--account{left:410px;top:610px}
.icon{width:14px;height:14px;display:block}
.menu-btn{position:absolute;right:22px;top:24px;width:20px;height:12px;color:var(--ink)}
.back-btn{position:absolute;left:20px;top:22px;width:18px;height:14px;color:var(--ink)}
.screen-title{text-align:center;font-weight:700;font-size:14px;padding-top:22px}
.btn{display:inline-block;background:linear-gradient(90deg,var(--green-dark),var(--green));color:#fff;font-weight:500;border-radius:14px;text-align:center}
.btn--save{position:absolute;left:70px;right:70px;bottom:40px;height:30px;line-height:30px;font-size:11px}
.btn--quote{font-size:8px;height:18px;line-height:18px;padding:0 12px}
.stars{color:var(--star);font-size:9px;letter-spacing:1px}
.stars small{color:var(--muted);font-size:8px;letter-spacing:0}
.badge{background:var(--green);color:#fff;font-size:7px;font-weight:500;border-radius:8px;padding:2px 6px;vertical-align:middle}
.round{width:20px;height:20px;border-radius:50%;display:flex;align-items:center;justify-content:center;color:#fff}
.round--green{background:var(--green)}
.round--grey{background:var(--icon-grey)}
.round .icon{width:10px;height:10px}
.photo{background:linear-gradient(135deg,var(--leaf-light),#3f9a2c 45%,var(--leaf-dark))}
.photo--lawn{background:linear-gradient(160deg,#b9b9ae,#6f9e3f 45%,#3d7a22)}
.photo--garden{background:linear-gradient(140deg,#a9c86a,#4f8c33 50%,#6c7f4a)}

/* profile */
.hero{position:absolute;left:0;top:0;width:340px;height:260px}
.hero-label{position:absolute;left:0;right:0;top:22px;text-align:center;color:#fff;font-weight:700;font-size:14px}
.hero .back-btn,.hero .menu-btn{color:#fff}
.hero-heart{position:absolute;right:52px;top:22px;width:16px;height:15px;color:#fff}
.hero-dots{position:absolute;right:24px;bottom:14px;display:flex;gap:5px;align-items:center}
.hero-dots i{width:5px;height:5px;border-radius:50%;background:rgba(255,255,255,.6)}
.hero-dots i.is-active{width:8px;height:8px;background:var(--green)}
.profile-thumb{position:absolute;left:20px;top:214px;width:92px;height:66px;border-radius:4px;border:3px solid #fff}
.profile-body{position:absolute;left:124px;right:20px;top:270px}
.biz-name{font-size:17px;font-weight:700}
.profile-about{font-size:7.5px;color:#555a60;line-height:1.45;margin:5px 0 8px}
.address{font-size:8px;font-weight:700;line-height:1.35}
.profile-actions{position:absolute;left:20px;top:300px;display:flex;flex-direction:column;gap:8px}
.services{position:absolute;left:20px;right:20px;top:430px}
.services h3{font-size:17px;font-weight:700;margin-bottom:5px}
.services p{font-size:8px;font-weight:500;line-height:1.4}

/* business profile form */
.form{position:absolute;left:30px;right:30px;top:70px}
.field{display:flex;justify-content:space-between;align-items:flex-end;border-bottom:1px solid var(--line);font-size:9px;color:#4a4e54;height:26px;padding-bottom:4px}
.field-row{display:flex;gap:16px}
.field-row .field{flex:1}
.chev{width:8px;height:8px;color:#4a4e54}
.textarea{border:1px solid var(--line);height:46px;margin-top:12px;padding:6px;font-size:7.5px;color:#b0b3b8}
.remove-link{text-align:right;font-size:7.5px;color:var(--green);margin-top:4px}
.connect-list{margin-top:10px;display:flex;flex-direction:column;gap:10px}
.connect{display:flex;align-items:center;gap:10px;font-size:9px;color:#4a4e54}
.connect .round--dark{background:#2b2e33}

/* listing */
.search{position:absolute;left:20px;right:60px;top:22px;border-bottom:1px solid var(--green);padding-bottom:5px;font-size:10px;display:flex;gap:6px;align-items:center}
.search b{font-weight:500}
.search span{color:#b0b3b8}
.search .icon{width:10px;height:10px;color:var(--muted)}
.listing{position:absolute;left:20px;right:16px;top:56px;display:flex;flex-direction:column;gap:12px}
.item{display:flex;gap:10px;position:relative}
.item-thumb{width:88px;height:68px;flex:none;border-radius:2px}
.item-info{flex:1;font-size:7.5px;color:#6a6e74;line-height:1.35}
.item-info h4{font-size:12px;color:var(--ink);font-weight:700;margin-bottom:1px}
.item-info .address{color:var(--ink);font-size:7.5px;margin:2px 0 5px}
.item-distance{position:absolute;right:0;top:0;font-size:7px;color:var(--muted)}
.item-icons{position:absolute;right:0;top:24px;display:flex;gap:5px}
.item-icons .round{width:17px;height:17px}

/* account */
.avatar{position:absolute;left:120px;top:70px;width:100px;height:70px;border-radius:3px}
.btn--change{position:absolute;left:135px;top:150px;height:20px;line-height:20px;font-size:8px;padding:0 20px}
.settings{position:absolute;left:30px;right:30px;top:200px}
.setting{display:flex;justify-content:space-between;align-items:center;border-bottom:1px solid var(--line);height:38px;font-size:10px;color:#4a4e54}

/* brand */
.brand{position:absolute;left:790px;top:530px;width:380px;display:flex;align-items:center;justify-content:flex-end;gap:14px}
.brand-mark{width:26px;height:26px;border-radius:50%;background:var(--green)}
.brand-name{font-weight:400;font-size:42px;line-height:1;color:var(--ink)}
</style>
</head>
<body>

<svg width="0" height="0" style="position:absolute" aria-hidden="true">
  <symbol id="i-menu" viewBox="0 0 20 12"><path d="M2 3h16M2 9h16" stroke="currentColor" stroke-width="2" stroke-linecap="round"/></symbol>
  <symbol id="i-back" viewBox="0 0 18 14"><path d="M17 7H2M7 2L2 7l5 5" fill="none" stroke="currentColor" stroke-width="1.6" stroke-linecap="round" stroke-linejoin="round"/></symbol>
  <symbol id="i-heart" viewBox="0 0 16 15"><path d="M8 13.5S1.5 9.5 1.5 5A3.2 3.2 0 0 1 8 3.6 3.2 3.2 0 0 1 14.5 5C14.5 9.5 8 13.5 8 13.5z" fill="none" stroke="currentColor" stroke-width="1.5"/></symbol>
  <symbol id="i-phone" viewBox="0 0 10 10"><path d="M2 1l2 2-1 1.2a6 6 0 0 0 2.8 2.8L7 6l2 2-1.2 1.3C4.5 9 1 5.5.7 2.2z" fill="currentColor"/></symbol>
  <symbol id="i-msg" viewBox="0 0 10 10"><rect x="1" y="2" width="8" height="6" rx="1" fill="none" stroke="currentColor" stroke-width="1.2"/><path d="M1.5 2.5L5 5.2l3.5-2.7" fill="none" stroke="currentColor" stroke-width="1"/></symbol>
  <symbol id="i-share" viewBox="0 0 10 10"><circle cx="2.5" cy="5" r="1.4" fill="currentColor"/><circle cx="7.5" cy="2" r="1.4" fill="currentColor"/><circle cx="7.5" cy="8" r="1.4" fill="currentColor"/><path d="M2.5 5L7.5 2M2.5 5l5 3" stroke="currentColor" stroke-width="1"/></symbol>
  <symbol id="i-chev-down" viewBox="0 0 8 8"><path d="M1 2.5l3 3 3-3" fill="none" stroke="currentColor" stroke-width="1.2"/></symbol>
  <symbol id="i-chev-right" viewBox="0 0 8 8"><path d="M2.5 1l3 3-3 3" fill="none" stroke="currentColor" stroke-width="1.2"/></symbol>
  <symbol id="i-search" viewBox="0 0 10 10"><circle cx="4.2" cy="4.2" r="3" fill="none" stroke="currentColor" stroke-width="1.3"/><path d="M6.5 6.5L9 9" stroke="currentColor" stroke-width="1.3"/></symbol>
</svg>

<!-- Business profile detail -->
<section class="screen screen--profile">
  <div class="hero photo" role="img" aria-label="Close-up photo of green grass blades">
    <svg class="back-btn"><use href="#i-back"/></svg>
    <div class="hero-label">Profile</div>
    <svg class="hero-heart"><use href="#i-heart"/></svg>
    <svg class="menu-btn"><use href="#i-menu"/></svg>
    <div class="hero-dots"><i></i><i></i><i class="is-active"></i><i></i></div>
  </div>
  <div class="profile-thumb photo--lawn" role="img" aria-label="Aerial photo of a lawn with a curving path"></div>
  <div class="profile-actions">
    <span class="round round--green"><svg class="icon"><use href="#i-phone"/></svg></span>
    <span class="round round--grey"><svg class="icon"><use href="#i-msg"/></svg></span>
    <span class="round round--green"><svg class="icon"><use href="#i-share"/></svg></span>
  </div>
  <div class="profile-body">
    <h2 class="biz-name">Thornfield Lawns <span class="badge">Sponsor</span></h2>
    <div class="stars">★★★★★ <small>(23)</small></div>
    <p class="profile-about">Friendly local team caring for lawns, borders and gardens all year round. We mow, feed, edge and tidy so your outdoor space always looks its very best.</p>
    <p class="address">14 Alder Row,<br>London E9 4QP</p>
    <span class="btn btn--quote" style="margin-top:8px">Request a Quote</span>
  </div>
  <div class="services">
    <h3>List of services</h3>
    <p>Pre-Emergents, Post-Emergents, Fertilization, Mowing<br>Watering, Aeration, Dethatching</p>
  </div>
</section>

<!-- Business profile form -->
<section class="screen screen--business">
  <svg class="back-btn" style="top:24px"><use href="#i-back"/></svg>
  <h1 class="screen-title">Business Profile</h1>
  <svg class="menu-btn"><use href="#i-menu"/></svg>
  <div class="form">
    <div class="field">Business Name</div>
    <div class="field-row">
      <div class="field">Address <svg class="chev"><use href="#i-chev-down"/></svg></div>
      <div class="field">State <svg class="chev"><use href="#i-chev-down"/></svg></div>
    </div>
    <div class="field">City</div>
    <div class="field">Zip Code</div>
    <div class="field">Phone Number</div>
    <div class="field">Website</div>
    <div class="textarea">Company Information</div>
    <div class="textarea">Service Offering (Please enter one service and comma)</div>
    <div class="remove-link">Remove</div>
    <div class="connect-list">
      <div class="connect"><span class="round round--green"></span>Connected</div>
      <div class="connect"><span class="round round--dark"></span>Connect to Plexo</div>
      <div class="connect"><span class="round round--dark"></span>Connect to Linkora</div>
    </div>
  </div>
  <span class="btn btn--save">Save</span>
</section>

<!-- Search results -->
<section class="screen screen--listing">
  <div class="search"><svg class="icon"><use href="#i-search"/></svg><b>Find</b><span>service, nearby</span></div>
  <svg class="menu-btn"><use href="#i-menu"/></svg>
  <div class="listing">
    <article class="item">
      <div class="item-thumb photo--lawn" role="img" aria-label="Aerial photo of a lawn with a curving path"></div>
      <div class="item-info">
        <h4>Thornfield Lawns <span class="badge">Sponsor</span></h4>
        <div class="stars">★★★★★ <small>(23)</small></div>
        Indoor, Outdoor Landscaping and more.
        <p class="address">14 Alder Row,<br>London E9 4QP</p>
        <span class="btn btn--quote">Request a Quote</span>
      </div>
      <span class="item-distance">2.1 mi</span>
      <div class="item-icons"><span class="round round--green"><svg class="icon"><use href="#i-phone"/></svg></span><span class="round round--grey"><svg class="icon"><use href="#i-msg"/></svg></span><span class="round round--green"><svg class="icon"><use href="#i-share"/></svg></span></div>
    </article>
    <article class="item">
      <div class="item-thumb photo" role="img" aria-label="Photo of a neatly trimmed grass bank"></div>
      <div class="item-info">
        <h4>Fernway Gardens</h4>
        <div class="stars">★★★★★ <small>(15)</small></div>
        Landscaping and Interior Design
        <p class="address">31 Birch Mews,<br>London N7 2LD</p>
        <span class="btn btn--quote">Request a Quote</span>
      </div>
      <span class="item-distance">3.6 mi</span>
      <div class="item-icons"><span class="round round--green"><svg class="icon"><use href="#i-phone"/></svg></span><span class="round round--green"><svg class="icon"><use href="#i-msg"/></svg></span><span class="round round--green"><svg class="icon"><use href="#i-share"/></svg></span></div>
    </article>
    <article class="item">
      <div class="item-thumb photo" role="img" aria-label="Close-up photo of green grass blades"></div>
      <div class="item-info">
        <h4>Cedarline Design</h4>
        <div class="stars">★★★★☆ <small>(09)</small></div>
        Landscaping and Interior Design
        <p class="address">8 Hollin Court,<br>Marsh Lane NW6</p>
        <span class="btn btn--quote">Request a Quote</span>
      </div>
      <span class="item-distance">5.5 mi</span>
      <div class="item-icons"><span class="round round--grey"><svg class="icon"><use href="#i-phone"/></svg></span><span class="round round--grey"><svg class="icon"><use href="#i-msg"/></svg></span><span class="round round--grey"><svg class="icon"><use href="#i-share"/></svg></span></div>
    </article>
    <article class="item">
      <div class="item-thumb photo--garden" role="img" aria-label="Aerial photo of a garden with trees and paths"></div>
      <div class="item-info">
        <h4>Mossbank Yards</h4>
        <div class="stars">★★★★☆ <small>(09)</small></div>
        Landscaping and Interior Design
        <p class="address">22 Orchard Hall, Linden Street NW3</p>
      </div>
      <span class="item-distance">4.6 mi</span>
    </article>
  </div>
</section>

<!-- Account settings -->
<section class="screen screen--account">
  <svg class="back-btn" style="top:24px"><use href="#i-back"/></svg>
  <h1 class="screen-title">Account Settings</h1>
  <svg class="menu-btn"><use href="#i-menu"/></svg>
  <div class="avatar photo--lawn" role="img" aria-label="Profile photo of a lawn with a curving path"></div>
  <span class="btn btn--change">Change</span>
  <div class="settings">
    <div class="setting">Profile <svg class="chev"><use href="#i-chev-right"/></svg></div>
    <div class="setting">Password <svg class="chev"><use href="#i-chev-right"/></svg></div>
    <div class="setting">Email Address <svg class="chev"><use href="#i-chev-right"/></svg></div>
    <div class="setting">Location <svg class="chev"><use href="#i-chev-right"/></svg></div>
    <div class="setting">Privacy Settings <svg class="chev"><use href="#i-chev-right"/></svg></div>
  </div>
  <span class="btn btn--save">Save</span>
</section>

<div class="brand">
  <span class="brand-mark" aria-hidden="true"></span>
  <div class="brand-name">Velmarigo</div>
</div>

</body>
</html>
```